Real Estate Investment Company Needs A Business Card Designed

I need a business card designed for my use. We are a real estate investment company based in Omaha, Nebraska that specializes in buying, rehabbing and selling single family and multifamily properties. Would love designs that incorporate our logo and colors

Industry/Entity Type

Business

Contact Information for Business Card

Mitchell Parkhurst | President & CEO
4873 North 52nd Avenue, Ste 700
Omaha, NE 68142
(402) 786-4259
mitchell@kestrelgateproperties.example
www.KestrelgateProperties.example

Font styles to use
Serif

Colors
0255a3
3276b5

Requirements
Must have
• Our logo

```html
<!DOCTYPE html>
<html lang="en">
<head>
<meta charset="utf-8">
<title>Kestrelgate Properties – Business Card</title>
<link rel="stylesheet" href="https://fonts.googleapis.com/css2?family=Lato:wght@400;700;900&display=swap">
<style>
  :root {
    --page-bg: #eceef1;
    --card-white: #ffffff;
    --brand-blue: #0255a3;
    --brand-blue-mid: #3276b5;
    --panel-top: #50a6f4;
    --panel-bottom: #2f7ccd;
    --text-light: #ffffff;
    --link-blue: #2a6fbe;
  }
  html, body {
    margin: 0;
    padding: 0;
    width: 1200px;
    height: 900px;
    overflow: hidden;
    background: var(--page-bg);
    font-family: "Lato", Arial, sans-serif;
  }
  .canvas {
    position: relative;
    width: 1200px;
    height: 900px;
  }
  .card {
    position: absolute;
    background: var(--card-white);
    box-shadow: 0 6px 18px rgba(0,0,0,0.18);
    overflow: hidden;
  }

  /* Front card */
  .card-front {
    left: 178px;
    top: 75px;
    width: 588px;
    height: 363px;
  }
  .front-brand {
    position: absolute;
    left: 0;
    top: 0;
    width: 152px;
    height: 100%;
    display: flex;
    flex-direction: column;
    align-items: center;
    justify-content: center;
    gap: 14px;
  }
  .brand-dot {
    width: 96px;
    height: 96px;
    border-radius: 50%;
    background: var(--brand-blue-mid);
  }
  .front-brand .brand-name {
    font-size: 15px;
    font-weight: 900;
    color: var(--brand-blue);
    letter-spacing: 0.5px;
    text-align: center;
    line-height: 1.2;
  }
  .front-panel {
    position: absolute;
    left: 152px;
    top: 0;
    right: 0;
    bottom: 0;
    background: linear-gradient(180deg, var(--panel-top), var(--panel-bottom));
    color: var(--text-light);
    text-align: right;
  }
  .person-name {
    position: absolute;
    right: 26px;
    top: 47px;
    margin: 0;
    font-size: 21px;
    font-weight: 700;
    letter-spacing: 0.3px;
    text-transform: uppercase;
  }
  .person-title {
    position: absolute;
    right: 26px;
    top: 72px;
    margin: 0;
    font-size: 15px;
  }
  .address {
    position: absolute;
    right: 26px;
    top: 200px;
    margin: 0;
    font-style: normal;
    font-size: 16px;
    line-height: 22px;
  }
  .contact-list {
    position: absolute;
    right: 24px;
    top: 263px;
    margin: 0;
    padding: 0;
    list-style: none;
    font-size: 16px;
    line-height: 21px;
  }
  .contact-list li {
    display: flex;
    justify-content: flex-end;
    align-items: center;
    gap: 4px;
  }
  .contact-icon {
    width: 11px;
    height: 11px;
    fill: var(--text-light);
  }

  /* Back card */
  .card-back {
    left: 388px;
    top: 505px;
    width: 567px;
    height: 352px;
    display: flex;
    flex-direction: column;
    align-items: center;
  }
  .back-brand {
    margin-top: 52px;
    display: flex;
    flex-direction: column;
    align-items: center;
  }
  .back-brand .brand-dot {
    width: 140px;
    height: 140px;
  }
  .back-brand .brand-name {
    margin-top: 20px;
    font-size: 30px;
    font-weight: 900;
    color: var(--brand-blue-mid);
    letter-spacing: 0.5px;
    line-height: 1;
    text-transform: uppercase;
  }
  .back-web {
    margin-top: 36px;
    font-size: 16px;
    color: var(--link-blue);
  }
</style>
</head>
<body>
<main class="canvas">

  <section class="card card-front" aria-label="Business card front">
    <div class="front-brand">
      <div class="brand-dot" aria-hidden="true"></div>
      <div class="brand-name">KESTRELGATE<br>PROPERTIES</div>
    </div>
    <div class="front-panel">
      <h1 class="person-name">Mitchell Parkhurst</h1>
      <p class="person-title">President &amp; CEO</p>
      <address class="address">
        4873 North 52nd Avenue, Ste 700<br>
        Omaha, NE 68142
      </address>
      <ul class="contact-list">
        <li>(402) 786-4259
          <svg class="contact-icon" viewBox="0 0 12 12" aria-hidden="true"><path d="M1 4c0-2 2-3 5-3s5 1 5 3v1H8V4H4v1H1z M3 6h6l2 5H1z"/></svg>
        </li>
        <li>mitchell@kestrelgateproperties.example
          <svg class="contact-icon" viewBox="0 0 12 12" aria-hidden="true"><path d="M1 3h10v7H1z M1 3l5 4 5-4" stroke="#2f7ccd" stroke-width="1"/></svg>
        </li>
        <li>www.KestrelgateProperties.example
          <svg class="contact-icon" viewBox="0 0 12 12" aria-hidden="true"><circle cx="6" cy="6" r="5.5"/></svg>
        </li>
      </ul>
    </div>
  </section>

  <section class="card card-back" aria-label="Business card back">
    <div class="back-brand">
      <div class="brand-dot" aria-hidden="true"></div>
      <div class="brand-name">Kestrelgate Properties</div>
    </div>
    <div class="back-web">www.KestrelgateProperties.example</div>
  </section>

</main>
</body>
</html>
```